Inspiring book cover design (business book for designers and innovators)

I'm writing my first book, to be published early next year. I'm struggling to come up with an inspiring book cover design. I need your help!

Information to be included on the cover:
Book Title: Bright maker's manual
Subtitle: Designing products and services that make sense
Author: Marianne Colt
Optional (not sure yet if I should include this on the cover): with online toolset

The book will be a square, size 170 x 170 mm
In the uploaded file you can find some example pages from the inside of the book. The cover design should fit with the design style of the example pages. The cover should "jump out" from the shelve in a bookstore and should attract designers, innovators, product managers, developers, and startup founders to buy the book.
Publisher: www.quillmarkpress.example

About the book:
Why do some products fail while others become a success? Why do so many companies launch crappy products and services that nobody wants? This book is both a guide to and a source of inspiration for, designing products and services that make sense. Because if they make sense to people, people will want them.
In order for tech products and services to make sense, and create value for users, we need to apply technologies in a meaningful way. We can achieve this by designing strong benefits and at the same time minimizing resistance users might have against new technologies.
This book offers a complete overview of how to develop products and services that make sense: 27 ways to strengthen benefits and 28 ways to mitigate resistance. It offers practical insights, examples, tips, and tools to design products and services that people will love to use.

About the author:
https://www.linkedin.example/in/mariannecolt/

Target Market(s)

designers, innovators, product managers, developers, and startup founders

Industry/Entity Type

Design Agency

Font styles to use
Other font styles liked:
• You can choose. The inside of the book uses 3 fonts: LuloCleanW01-OneBold, Sansation, Segoe UI

Requirements
Must have
• Clean, yet creative design.
Square shape
Fits the design style of the example pages
Sans serif fonts. Do not have to be the same fonts like the ones that are used inside the book (LuloCleanW01-OneBold, Sansation, Segoe UI), but should go well with them.

Bright makers manual
55 ways to design products and services that make sense
Marianne Colt
Nice to have
• I have several ideas that you might take as a starting point:
1) Do something with the left brain (rational, more digital) - right brain (creative, more emotional). For products to make sense, it needs to appeal to both parts of the brain
2) Work with a pattern, for example a (polygonal) triangular pattern
3) playful element in the letters, for example turning the O in innovator's into an on-off button or a stylish smiley, flipping the N in innovator's, doing something playful with the ' in innovator's
I've uploaded some images as a source of inspiration.

The cover should have a different color than the red/blue used in the example pages, but should fit the color palette that is used in the example pages.
Trigger curiosity.
Should not have
• Photographic pictures

```html
<!DOCTYPE html>
<html lang="en">
<head>
<meta charset="utf-8">
<title>Bright Makers Manual — Cover Spread</title>
<link href="https://fonts.googleapis.com/css2?family=Ubuntu:wght@500;700&family=Exo+2:wght@400;500&family=Noto+Sans:wght@400&display=swap" rel="stylesheet">
<style>
  :root {
    --ink: #000000;
    --paper: #ffffff;
    --accent: #9c1f3d;
    --accent-soft: #b8475f;
    --steel: #a7a7ab;
    --spine: #3a3a3a;
  }
  html, body {
    margin: 0;
    padding: 0;
    width: 1200px;
    height: 599px;
    overflow: hidden;
    background: var(--ink);
  }
  .spread {
    position: relative;
    width: 1200px;
    height: 599px;
    background: var(--ink);
    color: var(--paper);
  }
  .spine-fold {
    position: absolute;
    left: 601px;
    top: 0;
    width: 1px;
    height: 599px;
    background: var(--spine);
  }

  /* Back cover */
  .back-cover {
    position: absolute;
    left: 0;
    top: 0;
    width: 601px;
    height: 599px;
  }
  .blurb-frame {
    position: absolute;
    left: 107px;
    top: 80px;
    width: 388px;
    height: 335px;
  }
  .blurb {
    position: absolute;
    left: 118px;
    top: 100px;
    width: 366px;
    font-family: "Noto Sans", sans-serif;
    font-size: 12.6px;
    line-height: 15px;
    text-align: center;
    color: var(--paper);
  }
  .blurb p {
    margin: 0 0 15px 0;
  }
  .frame-emblem {
    position: absolute;
    left: 278px;
    top: 396px;
    width: 46px;
    height: 46px;
    border-radius: 50%;
    background: radial-gradient(circle, var(--accent-soft) 0%, var(--accent) 70%);
  }
  .toolset-note,
  .publisher {
    position: absolute;
    left: 0;
    width: 601px;
    text-align: center;
    font-family: "Exo 2", sans-serif;
    font-size: 15px;
    color: var(--paper);
  }
  .toolset-note { top: 485px; }
  .publisher { top: 525px; }

  /* Front cover */
  .front-cover {
    position: absolute;
    left: 602px;
    top: 0;
    width: 598px;
    height: 599px;
  }
  .title {
    position: absolute;
    left: 0;
    top: 50px;
    width: 598px;
    margin: 0;
    text-align: center;
    font-family: "Ubuntu", sans-serif;
    font-weight: 700;
    color: var(--paper);
    line-height: 1;
  }
  .title span { display: block; }
  .title .line-one { font-size: 80px; height: 78px; letter-spacing: 1px; }
  .title .line-two { font-size: 66px; height: 68px; letter-spacing: 1px; }
  .title .line-three { font-size: 70px; height: 70px; letter-spacing: 1px; }

  .count-rule {
    position: absolute;
    top: 325px;
    height: 2px;
    background: var(--accent);
  }
  .count-rule.left { left: 91px; width: 152px; }
  .count-rule.right { left: 353px; width: 152px; }

  .count-emblem {
    position: absolute;
    left: 250px;
    top: 278px;
    width: 96px;
    height: 96px;
    border-radius: 50%;
    background: radial-gradient(circle, #2b2b2d 0%, #4a4a4e 60%, var(--steel) 100%);
    opacity: 0.55;
  }
  .count-number {
    position: absolute;
    left: 250px;
    top: 288px;
    width: 96px;
    text-align: center;
    font-family: "Ubuntu", sans-serif;
    font-weight: 500;
    font-size: 40px;
    color: var(--accent);
  }
  .subtitle {
    position: absolute;
    left: 0;
    top: 382px;
    width: 598px;
    margin: 0;
    text-align: center;
    font-family: "Exo 2", sans-serif;
    font-weight: 500;
    font-size: 32px;
    line-height: 38px;
    color: var(--paper);
  }
  .author {
    position: absolute;
    left: 0;
    top: 522px;
    width: 598px;
    text-align: center;
    font-family: "Ubuntu", sans-serif;
    font-weight: 500;
    font-size: 22px;
    color: var(--accent);
  }
</style>
</head>
<body>
<main class="spread">

  <section class="back-cover">
    <svg class="blurb-frame" viewBox="0 0 388 335" width="388" height="335" aria-hidden="true">
      <path d="M158 333 H1 V1 H387 V333 H230"
            fill="none" stroke="#9c1f3d" stroke-width="1.4" stroke-dasharray="1.4 1.6"/>
    </svg>

    <div class="blurb">
      <p>Why do some products fail while others become a success? Why do so many companies launch crappy products and services that nobody wants?</p>
      <p>This book is both a guide to and a source of inspiration for, designing products and services that make sense. Because if they make sense to people, people will want them.</p>
      <p>In order for tech products and services to make sense, and create value for users, we need to apply technologies in a meaningful way. We can achieve this by designing strong benefits and at the same time minimizing resistance users might have against new technologies.</p>
      <p>This book offers a complete overview of how to develop products and services that make sense: 27 ways to strengthen benefits and 28 ways to mitigate resistance. It offers practical insights, examples, tips, and tools to design products and services that people will love to use.</p>
    </div>

    <div class="frame-emblem" role="img" aria-label="Small crimson lightbulb emblem with a gear and orbiting rings"></div>

    <div class="toolset-note">with free online toolset</div>
    <div class="publisher">Publisher: www.quillmarkpress.example</div>
  </section>

  <div class="spine-fold"></div>

  <section class="front-cover">
    <h1 class="title">
      <span class="line-one">BRIGHT</span>
      <span class="line-two">MAKERS</span>
      <span class="line-three">MANUAL</span>
    </h1>

    <div class="count-rule left"></div>
    <div class="count-rule right"></div>
    <div class="count-emblem" role="img" aria-label="Grey outline lightbulb with orbiting atom rings around the number"></div>
    <div class="count-number">55</div>

    <p class="subtitle">ways to design<br>products and services<br>that make sense</p>

    <div class="author">Marianne Colt</div>
  </section>

</main>
</body>
</html>
```